Updated flyer

we are a defence industry trainer and we are updating a course that has been running for a few years, so want a new look flyer. Please note that the flyer is A4 and we would like people to fill in the document online. Please add a tickbox for SME's free and add a call out box saying the course is NEW & UPDATED.

Industry/Entity Type

Defence

Font styles to use
Sans Serif
Other font styles liked:
• AVENIR

Colors
3176b5
01a88e
9bcb3b
fbed22
f37022

```html
<!DOCTYPE html>
<html lang="en">
<head>
<meta charset="utf-8">
<title>Defence, ITAR &amp; EAR Training Controls – Course Flyer</title>
<link rel="stylesheet" href="https://fonts.googleapis.com/css2?family=Dosis:wght@400;500;600;700&family=PT+Serif:ital,wght@0,400;0,700;1,400&family=Roboto+Slab:wght@700&family=Arimo:wght@400;700&display=swap">
<style>
  :root {
    --brand-blue: #2389b4;
    --band-blue: #2c8cb6;
    --deep-teal: #17708f;
    --brand-green: #3f9a3c;
    --callout-orange: #f37022;
    --ink: #1d1d1d;
    --ink-soft: #3a3a3a;
    --rule: #7fb6d2;
    --paper: #ffffff;
    --photo-light: #e9eef2;
    --photo-mid: #b9c9d6;
    --photo-dark: #6d8397;
  }
  * { box-sizing: border-box; margin: 0; padding: 0; }
  html, body { width: 849px; height: 1200px; overflow: hidden; background: var(--paper); }
  .flyer {
    position: relative;
    width: 849px;
    height: 1200px;
    overflow: hidden;
    background: var(--paper);
    border: 1px solid var(--rule);
    font-family: "PT Serif", Georgia, serif;
    color: var(--ink);
  }

  /* Brand lockup */
  .brand {
    position: absolute;
    top: 72px; left: 0; width: 100%;
    display: flex; justify-content: center; align-items: center; gap: 16px;
  }
  .brand-mark {
    width: 60px; height: 60px; border-radius: 50%;
    background: var(--brand-green);
  }
  .brand-name {
    font-family: "Dosis", Arial, sans-serif;
    font-weight: 600; font-size: 38px; letter-spacing: 0.5px;
    color: var(--brand-green);
  }

  /* Headline */
  .headline {
    position: absolute; top: 194px; left: 0; width: 100%;
    text-align: center; line-height: 52px;
    font-family: "Dosis", Arial, sans-serif;
    font-weight: 600; font-size: 44px; letter-spacing: 0.8px;
    color: var(--brand-blue);
  }
  .subhead {
    position: absolute; top: 240px; left: 0; width: 100%;
    text-align: center; line-height: 42px;
    font-family: "Dosis", Arial, sans-serif;
    font-weight: 400; font-size: 34px; letter-spacing: 1.6px;
    color: var(--ink-soft);
  }

  /* Intro copy */
  .intro {
    position: absolute; top: 292px; left: 33px; width: 783px;
    font-size: 15.5px; line-height: 22px; text-align: justify;
  }
  .intro p + p { margin-top: 8px; }
  .intro .lead {
    font-family: "Roboto Slab", Georgia, serif;
    font-weight: 700; font-size: 18px;
    color: var(--brand-blue);
  }

  /* Photo area */
  .hero-photo {
    position: absolute; top: 459px; left: 13px; width: 823px; height: 322px;
    border-top: 2px solid var(--rule);
    background: linear-gradient(120deg, var(--photo-light) 0%, var(--photo-mid) 45%, var(--photo-dark) 70%, var(--photo-light) 100%);
  }

  /* NEW & UPDATED callout */
  .callout {
    position: absolute; top: 478px; right: 34px;
    padding: 10px 18px;
    background: var(--callout-orange); color: var(--paper);
    border: 3px solid var(--paper);
    border-radius: 6px;
    font-family: "Dosis", Arial, sans-serif;
    font-weight: 700; font-size: 26px; letter-spacing: 1px; line-height: 30px;
  }

  /* Testimonials */
  .testimonials {
    position: absolute; top: 800px; left: 30px; width: 518px;
    list-style: none; text-align: right;
    font-style: italic; font-size: 16.5px; line-height: 29.5px;
    color: var(--ink-soft);
  }
  .testimonials-rule {
    position: absolute; top: 954px; left: 40px; width: 510px;
    border-top: 1px solid var(--rule);
  }

  /* Schedule */
  .schedule {
    position: absolute; top: 797px; left: 563px; width: 260px;
    border-collapse: collapse;
    border-left: 2px solid var(--brand-blue);
    font-family: "Arimo", Arial, sans-serif;
    font-size: 17.5px; color: var(--ink);
  }
  .schedule td { padding: 0 0 0 10px; height: 29.5px; white-space: nowrap; }
  .schedule .city { width: 88px; padding-right: 6px; border-right: 2px solid var(--brand-blue); }

  /* Pricing */
  .price {
    position: absolute; top: 962px; left: 0; width: 100%;
    text-align: center; color: var(--deep-teal); line-height: 52px;
    font-family: "PT Serif", Georgia, serif; font-size: 38px;
  }
  .price .amount { font-family: "Roboto Slab", Georgia, serif; font-weight: 700; font-size: 42px; }
  .price .tax { font-size: 24px; }

  .sme-band {
    position: absolute; top: 1022px; left: 13px; width: 823px; height: 42px;
    background: var(--band-blue); color: var(--paper);
    display: flex; align-items: center; justify-content: center; gap: 12px;
    font-size: 26px; cursor: pointer;
  }
  .sme-band strong { font-weight: 700; letter-spacing: 0.5px; }
  .sme-tick {
    appearance: none; -webkit-appearance: none;
    width: 24px; height: 24px; flex: none;
    border: 2px solid var(--paper); border-radius: 3px;
    background: transparent; cursor: pointer; position: relative;
  }
  .sme-tick:checked { background: var(--paper); }
  .sme-tick:checked::after {
    content: ""; position: absolute; left: 6px; top: 1px;
    width: 7px; height: 13px;
    border: solid var(--band-blue); border-width: 0 3px 3px 0;
    transform: rotate(45deg);
  }

  /* Footer */
  .subsidy {
    position: absolute; top: 1085px; left: 0; width: 100%;
    text-align: center; font-family: "Arimo", Arial, sans-serif; font-size: 18px;
  }
  .contact-prompt {
    position: absolute; top: 1118px; left: 0; width: 100%;
    text-align: center; font-family: "Arimo", Arial, sans-serif; font-size: 17px;
  }
  .contact-line {
    position: absolute; top: 1145px; left: 0; width: 100%;
    text-align: center; white-space: nowrap;
    font-family: "Arimo", Arial, sans-serif;
    font-size: 23px; font-weight: 700; color: var(--ink);
  }
  .contact-line .on { font-weight: 400; font-size: 18px; }
</style>
</head>
<body>
<main class="flyer">
  <div class="brand">
    <span class="brand-mark"></span>
    <span class="brand-name">Meridian Trade Compliance Institute</span>
  </div>

  <h1 class="headline">DEFENCE, ITAR &amp; EAR TRAINING CONTROLS</h1>
  <h2 class="subhead">FROM A NON-U.S. PERSPECTIVE TRAINING</h2>

  <section class="intro">
    <p><span class="lead">U.S. Export Controls</span> are some of the most complex and stringent in the world. The U.S. Government regulates the transfer of U.S. origin goods and technical data throughout the world, with the intent of preventing unauthorised transfer of technology and know-how. These controls extend world-wide and can impact anyone dealing in U.S. controlled goods or technology.</p>
    <p><span class="lead">This two-day comprehensive course</span> will give applicants a greater understanding of U.S. Export Controls from a non-U.S. perspective in practical and relevant terms.</p>
  </section>

  <div class="hero-photo" role="img" aria-label="Photo of a smiling group of business professionals seated at a training session"></div>
  <div class="callout">NEW &amp; UPDATED</div>

  <ul class="testimonials">
    <li>“Excellent structure and style of presentation.”</li>
    <li>“Excellent...best U.S export controls training I have attended.”</li>
    <li>“Practical workshops were fantastic.”</li>
    <li>“Excellent presenter and coordination.”</li>
    <li>“Very informative, well presented course.”</li>
  </ul>
  <div class="testimonials-rule"></div>

  <table class="schedule">
    <tr><td class="city">Brisbane</td><td>16 &amp; 17 March</td></tr>
    <tr><td class="city">Sydney</td><td>18 &amp; 19 March</td></tr>
    <tr><td class="city">Canberra</td><td>20 &amp; 23 March</td></tr>
    <tr><td class="city">Melbourne</td><td>24 &amp; 25 March</td></tr>
    <tr><td class="city">Adelaide</td><td>26 &amp; 27 March</td></tr>
  </table>

  <p class="price"><span class="amount">$1295.00 AUD</span> per person <span class="tax">(inc GST)</span></p>

  <label class="sme-band">
    <input class="sme-tick" type="checkbox" name="sme-free">
    <span>Small to Medium Enterprises <strong>FREE OF CHARGE</strong></span>
  </label>

  <p class="subsidy">Subsidised by the Regional Industry Capability Fund (RICF)</p>
  <p class="contact-prompt">For more information, please contact</p>
  <p class="contact-line">MTCI <span class="on">on</span> +61 (0)7 5550 1837 | info@mtci.com.au | www.mtci.com.au</p>
</main>
</body>
</html>
```